Providing Back Office Solutions to Financial Advisors and Attorney Needs a Business Card Design

Need a Business Card Design that speaks to Financial Advisor and Attorneys. Some of the word that come to mind is Clean/Simple & Futuristic.

Industry/Entity Type

Business

```html
<!DOCTYPE html>
<html lang="en">
<head>
<meta charset="utf-8">
<title>Orvane Back Office Solutions – Business Card</title>
<link href="https://fonts.googleapis.com/css2?family=Oswald:wght@500&family=Open+Sans:wght@400;600&display=swap" rel="stylesheet">
<style>
  :root {
    --backdrop: #e4e6e9;
    --card: #ffffff;
    --brand-blue: #1a7cc0;
    --brand-navy: #2b4f9c;
    --text-grey: #5c5f63;
    --rule-grey: #8a8d91;
    --shadow: rgba(0, 0, 0, 0.18);
  }
  * { box-sizing: border-box; margin: 0; padding: 0; }
  html, body { width: 1200px; height: 904px; overflow: hidden; }
  body {
    background: var(--backdrop);
    font-family: "Open Sans", Arial, sans-serif;
    position: relative;
  }
  .card {
    position: absolute;
    width: 560px;
    height: 320px;
    background: var(--card);
    box-shadow: 0 10px 28px var(--shadow);
  }
  .card-front { left: 90px; top: 100px; }
  .card-back { left: 550px; top: 480px; }

  /* Front */
  .brand-lockup {
    position: absolute;
    left: 50%; top: 50%;
    transform: translate(-50%, -50%);
    display: flex;
    align-items: center;
    gap: 14px;
  }
  .brand-square {
    width: 44px; height: 44px;
    background: var(--brand-blue);
  }
  .brand-divider {
    width: 1px; height: 62px;
    background: var(--brand-navy);
  }
  .brand-name {
    font-family: "Open Sans", Arial, sans-serif;
    font-weight: 600;
    font-size: 38px;
    letter-spacing: 3px;
    line-height: 1;
    color: var(--brand-blue);
  }
  .brand-tagline {
    margin-top: 6px;
    font-size: 12.5px;
    letter-spacing: 0.5px;
    color: var(--brand-navy);
  }

  /* Back */
  .identity {
    position: absolute;
    left: 120px; top: 112px;
    text-align: right;
  }
  .person-name {
    font-family: "Oswald", Impact, sans-serif;
    font-weight: 500;
    font-size: 30px;
    line-height: 1;
    color: var(--brand-blue);
  }
  .person-title {
    font-size: 12px;
    color: var(--text-grey);
    margin-top: 2px;
  }
  .identity-divider {
    position: absolute;
    left: 282px; top: 92px;
    width: 1px; height: 74px;
    background: var(--rule-grey);
  }
  .contact-list {
    position: absolute;
    left: 300px; top: 92px;
    list-style: none;
  }
  .contact-item {
    display: flex;
    align-items: center;
    gap: 9px;
    font-size: 13px;
    color: var(--text-grey);
    height: 22px;
  }
  .contact-icon { width: 12px; height: 12px; flex: none; }
  .address {
    position: absolute;
    right: 40px; bottom: 38px;
    font-size: 13px;
    color: var(--text-grey);
  }
</style>
</head>
<body>
  <section class="card card-front" aria-label="Card front">
    <div class="brand-lockup">
      <div class="brand-square"></div>
      <div class="brand-divider"></div>
      <div class="brand-text">
        <div class="brand-name">ORVANE</div>
        <div class="brand-tagline">BACK OFFICE SOLUTIONS</div>
      </div>
    </div>
  </section>

  <section class="card card-back" aria-label="Card back">
    <div class="identity">
      <div class="person-name">JOHN SMITH</div>
      <div class="person-title">Manager</div>
    </div>
    <div class="identity-divider"></div>
    <ul class="contact-list">
      <li class="contact-item">
        <svg class="contact-icon" viewBox="0 0 12 12"><circle cx="6" cy="6" r="6" fill="#1a7cc0"/><path d="M4 3.2l1 1.2-.6.8c.4.8 1 1.4 1.8 1.8l.8-.6 1.2 1-.6 1c-2.4-.3-4-1.9-4.3-4.3z" fill="#fff"/></svg>
        +999 9999 9999
      </li>
      <li class="contact-item">
        <svg class="contact-icon" viewBox="0 0 12 12"><circle cx="6" cy="6" r="6" fill="#1a7cc0"/><rect x="3" y="4" width="6" height="4.2" fill="#fff"/><path d="M3 4l3 2.3L9 4" stroke="#1a7cc0" stroke-width=".7" fill="none"/></svg>
        info@mywebsite.com
      </li>
      <li class="contact-item">
        <svg class="contact-icon" viewBox="0 0 12 12"><circle cx="6" cy="6" r="6" fill="#1a7cc0"/><circle cx="6" cy="6" r="3.2" stroke="#fff" stroke-width=".8" fill="none"/><path d="M2.8 6h6.4M6 2.8c-1.4 1.8-1.4 4.6 0 6.4M6 2.8c1.4 1.8 1.4 4.6 0 6.4" stroke="#fff" stroke-width=".7" fill="none"/></svg>
        www.mywebsite.com
      </li>
    </ul>
    <div class="address">99th Street, Exact Road, New cross side, CA 456982.</div>
  </section>
</body>
</html>
```